Corporate Design für valtrino financial services (vfs)
Kommunikation lief erstklassig. Super schnelle Antwort auf alle Fragen und unmittelbare Umsetzung von Wünschen/Korrekturen. Wir sind rundum zufrieden und sind KELDU sehr dankbar für die professionelle Betreuung. Weiter so!!!
Zielgruppe
Was wir machen:
Wir sind ein hochwertiger Finanzmakler, der seinen Mandaten in allen Bereichen zum Thema 'Finanzen und Versicherungen' mit Rat und Tat zur Seite steht. Vertrauen und Seriosität stehen dabei an erster Stelle.
Unsere Dienstleistung zielt darauf ab, der Ansprechpartner Nummer 1 zu sein, wenn es um Produkte aus dem Finanz- und Versicherungssektor geht. Gemäß dem Motto 'Ihr Ziel klar im Blick'.
Somit müssen sich unsere Mandanten nicht mit verschiedenen Banken und Versicherern auseinandersetzen und haben mit uns einen Ansprechpartner für alle Belange. Nach einer intensiven Anaylse der Ist-Situation erarbeiten wir im jeweiligen Bereich die optimale Lösung heraus und fassen diese schriftlich in einem Gesamtkonzept für unsere Mandanten zusammen. Somit erhält er eine übersichtliche Handlungsempfehlung von uns.
--> Kurz gesagt: Wir erstellen maßgeschneiderte Finanzkonzepte für Privatkunden, sowie für Klein- und Mittelständische Unternehmen.
Unsere Zielgruppe:
Da unsere Beratung fachlich und inhaltlich sehr anspruchsvoll ist, haben wir überwiegend (angehende) Akademiker und Selbstständige/Unternehmer in unserem Bestand. Daher ist unsere Zielgruppe eher im 'gebildeten Bereich' zu suchen, ohne groß wertend klingen zu wollen. Die Altersspanne liegt vermehrt zwischen 25-45 jahren.
Neben den Akademikern und den Unternehmern betreuen wir zunehmend Klein- und Mittelständische Unternehmen im Bereich 'Betriebliches Vorsorgemanagement'.
--> Kurz gesagt: (Angehende) Akademiker, Selbstständige/Unternehmer, Klein- & Mittelständische Unternehmen
Wer wir sind:
Ein überwiegend junges und dynamisches Team aus 12 Leuten im Alter zwischen 22 und 38. Lediglich unser 'Senior' hat so gerade die 40er-Marke übersprungen. Jeder von uns ist hoch motiviert stets die optimale Lösung für seine Mandanten herauszuarbeiten.
Aufgabenstellung
Nach 14 Jahren bei der 'valtrino GmbH Makler', werden wir uns nun mit einem Teil des Teams "abspalten" und die 'valtrino financial services' gründen.
Uns ist wichtig, dass mit dem Logo ein frischer Wind einhergeht und eine "Novation" zu erkennen ist. Dennoch soll weiterhin zu erkennen sein, dass wir nach wie vor im gleichen Sektor tätig sind und der Bruch nicht zu radikal ist.
Wir wollen also gerne nach wie vor als "valtrino" wahrgenommen werden, aber mit dem Logo muss klar werden, dass wir nicht mehr die alte "valtrino" sind. Diese wird nämlich nach wie vor bestehen bleiben, aber an anderen Standorten und mit leicht anderen Schwerpunkten ihre Mandaten beraten.
Wir werden in Hannover, Paderborn, Kassel und im Sauerland aktiv sein. Die alte valtrino in Köln, Magdeburg und Jena. Die Lösung wird also ein kleiner Drahtseilakt ;-)
Evtl. können Teile des alten Schriftzugs erhalten bleiben und mit neuer Farbe und dem Zusatz "financial services" verknüpft werden (Altes Logo ist beigefügt).
Die Farbe grün wird doch als neu und frisch wahrgenommen, oder?!
Wir sind aber auch gerne offen für alle anderen Ideen!!!

```html
<!DOCTYPE html>
<html lang="de">
<head>
<meta charset="utf-8">
<title>valtrino financial services – Corporate Design</title>
<link href="https://fonts.googleapis.com/css2?family=Source+Sans+3:ital,wght@0,400;0,700;0,800;1,400&display=swap" rel="stylesheet">
<style>
  :root {
    --brand-green: #008a36;
    --brand-green-faint: #dce6d6;
    --ink: #3a3a3c;
    --text: #2b2b2b;
    --paper: #ffffff;
    --shadow: 0 4px 12px rgba(0,0,0,0.35);
  }
  * { margin: 0; padding: 0; box-sizing: border-box; }
  html, body { width: 848px; height: 1200px; overflow: hidden; background: var(--paper); }
  body { position: relative; font-family: "Source Sans 3", "Myriad Pro", sans-serif; color: var(--text); }

  .wordmark { position: absolute; font-weight: 800; color: var(--brand-green); line-height: 1; letter-spacing: -0.01em; white-space: nowrap; }
  .tagline { position: absolute; color: var(--ink); font-style: italic; line-height: 1; white-space: nowrap; }

  /* Primary logo */
  .logo-main .wordmark { left: 0; width: 848px; text-align: center; font-size: 106px; top: 52px; }
  .logo-main .tagline { left: 0; width: 848px; text-align: center; top: 142px; font-size: 29px; padding-left: 40px; }

  /* Letterhead */
  .letterhead { position: absolute; left: 187px; top: 237px; width: 467px; height: 662px; background: var(--paper); box-shadow: var(--shadow); }
  .rule { position: absolute; height: 3px; background: var(--brand-green); }
  .letterhead .rule-left { left: 0; top: 44px; width: 253px; }
  .letterhead .rule-right { left: 428px; top: 44px; width: 39px; }
  .letterhead .wordmark { left: 260px; top: 17px; font-size: 37px; }
  .letterhead .tagline { left: 308px; top: 51px; font-size: 12px; }
  .sender-address { position: absolute; left: 306px; top: 78px; font-size: 7.2px; font-style: italic; line-height: 11.6px; }
  .return-line { position: absolute; left: 52px; top: 113px; font-size: 4.6px; font-style: italic; white-space: nowrap; display: flex; align-items: baseline; gap: 2px; }
  .return-line .wordmark { position: static; font-size: 11px; }
  .faint-mark { position: absolute; left: 322px; top: 512px; }
  .letterhead .rule-footer { left: 0; top: 616px; width: 467px; height: 1.4px; }
  .footer-col { position: absolute; top: 627px; font-size: 5px; font-style: italic; line-height: 7.6px; white-space: nowrap; }
  .footer-col.c1 { left: 50px; } .footer-col.c2 { left: 201px; } .footer-col.c3 { left: 326px; }

  /* Business cards */
  .card { position: absolute; top: 966px; width: 277px; height: 182px; box-shadow: var(--shadow); }
  .card-back { left: 115px; background: var(--brand-green); }
  .card-back .wordmark { color: var(--paper); left: 0; width: 277px; text-align: center; top: 68px; font-size: 44px; }
  .card-front { left: 455px; background: var(--paper); }
  .card-front .rule-left { left: 0; top: 69px; width: 142px; height: 2px; }
  .card-front .rule-right { left: 242px; top: 69px; width: 35px; height: 2px; }
  .card-front .wordmark { left: 148px; top: 54px; font-size: 20px; }
  .card-front .tagline { left: 172px; top: 74px; font-size: 7px; }
  .card-name { position: absolute; left: 80px; top: 108px; font-size: 9px; font-style: italic; white-space: nowrap; }
  .card-contact { position: absolute; left: 174px; top: 109px; font-size: 6.2px; font-style: italic; line-height: 10.4px; white-space: nowrap; }
  .card-front .rule-bottom-left { left: 0; top: 159px; width: 169px; height: 1.4px; }
  .card-front .rule-bottom-right { left: 237px; top: 159px; width: 40px; height: 1.4px; }
</style>
</head>
<body>

  <header class="logo-main">
    <div class="wordmark">valtrino</div>
    <div class="tagline">financial services</div>
  </header>

  <section class="letterhead" aria-label="Briefbogen">
    <div class="rule rule-left"></div>
    <div class="rule rule-right"></div>
    <div class="wordmark">valtrino</div>
    <div class="tagline">financial services</div>

    <address class="sender-address">
      Beispielstr. 123<br>
      54321 Musterstadt<br>
      +49 543 / 98 76 54 32<br>
      +49 123 / 12 34 56 78<br>
      kontakt@valtrino.de<br>
      www.valtrino.de
    </address>

    <div class="return-line">
      <span class="wordmark">valtrino</span>
      <span>| Beispielstraße 123 | 54321 Musterstadt</span>
    </div>

    <svg class="faint-mark" width="100" height="100" viewBox="0 0 100 100" aria-hidden="true">
      <circle cx="50" cy="50" r="48" fill="var(--brand-green-faint)"/>
    </svg>

    <div class="rule rule-footer"></div>
    <div class="footer-col c1">Hauptsitz<br>Beispielstraße 123, 54321 Musterstadt<br>Geschäftsführer: Max Mustermann</div>
    <div class="footer-col c2">Amtsgericht Musterstadt<br>HRB 000000 B<br>Steuernummer: 000/0000/0000</div>
    <div class="footer-col c3">Musterbank<br>IBAN: DE00 0000 0000 0000 0000 00<br>BIC: XXXXXXXXXXX</div>
  </section>

  <section class="card card-back" aria-label="Visitenkarte Rückseite">
    <div class="wordmark">valtrino</div>
  </section>

  <section class="card card-front" aria-label="Visitenkarte Vorderseite">
    <div class="rule rule-left"></div>
    <div class="rule rule-right"></div>
    <div class="wordmark">valtrino</div>
    <div class="tagline">financial services</div>
    <div class="card-name">Max Mustermann</div>
    <address class="card-contact">
      Beispielstr. 123<br>
      54321 Musterstadt<br>
      Fon +49 543 / 98 76 54 32<br>
      Mobil +49 123 / 12 34 56 78<br>
      kontakt@valtrino.de
    </address>
    <div class="rule rule-bottom-left"></div>
    <div class="rule rule-bottom-right"></div>
  </section>

</body>
</html>
```